Therapy Dog Organization Website

Looking for a website that is user friendly, welcoming, dog themed and has the following pages and links:
*Click here to join - links to a jot form
*Click here to donate - links to our paypal page
*Request a visit - links to a jot form
*Facebook Follow Link
*Instagram Follow Link
*Our team - images uploaded to showcase our dogs
*Donors and Referrals Page - Where I can update as donations and referrals come in.
*Online store. Currently this is in Jot Form but I would like a store front. I would not want this to be a link but rather a hidden page, something like www.hollowbirch.org/teamstore.

Please visit www.hollowbirch.org to see what we have right now designed simply in Canva. Dog photos can be provided to use in images.

Note: I have funds from a grant that I have to spend to add gratuity to the project winner.

```html
<!DOCTYPE html>
<html lang="en">
<head>
<meta charset="utf-8">
<title>Hollow Birch Therapy Dogs</title>
<link href="https://fonts.googleapis.com/css2?family=Outfit:wght@500;600;700&family=Poppins:wght@400;500;600&display=swap" rel="stylesheet">
<style>
:root{
  --pink:#f27a9f;
  --pink-soft:#fde3ec;
  --pink-band:#f6829f;
  --green:#6cbf5b;
  --green-soft:#e5f3df;
  --yellow:#f7c65c;
  --yellow-soft:#fdf1d3;
  --ink:#1d1f33;
  --text:#4a4d5c;
  --muted:#7b7e8c;
  --card:#faf8f4;
  --line:#efeae3;
  --footer:#f7f6f4;
}
*{box-sizing:border-box;margin:0;padding:0}
html,body{width:1200px;height:3592px;overflow:hidden}
body{background:#fff;font-family:"Poppins",sans-serif;color:var(--text);position:relative}
.abs{position:absolute}
h1,h2,h3,.logo-name{font-family:"Outfit",sans-serif;color:var(--ink)}
.eyebrow{font-size:11px;font-weight:600;letter-spacing:.5px;text-transform:uppercase;color:var(--pink);display:flex;align-items:center;gap:5px}
.eyebrow.green{color:var(--green)}
.eyebrow.gold{color:#d9a02c}
.btn{display:inline-flex;align-items:center;gap:8px;background:var(--pink);color:#fff;font-size:13px;font-weight:600;border-radius:10px;padding:0 22px;height:42px;text-decoration:none}
.btn.green{background:var(--green)}
.paw{width:14px;height:14px;fill:currentColor}
.photo{background:linear-gradient(135deg,#e8c48e,#c99559)}

/* header */
.logo{display:flex;align-items:center;gap:10px}
.logo-mark{width:34px;height:34px;border-radius:50%;background:var(--ink)}
.logo-name{font-size:28px;font-weight:600;line-height:1}
.logo-sub{font-family:"Outfit",sans-serif;font-size:15px;font-weight:600;color:var(--ink);letter-spacing:1.5px}
.top-links{top:44px;right:56px;display:flex;gap:40px}
.top-links a{font-size:11px;color:var(--text);text-decoration:none;display:flex;flex-direction:column;align-items:center;gap:4px}
.top-links svg{width:14px;height:14px;stroke:var(--pink);fill:none;stroke-width:2}
.nav{top:122px;left:332px;display:flex;gap:46px}
.nav a{font-size:13px;color:var(--ink);text-decoration:none;font-weight:500}
.nav a.active{color:var(--pink)}

/* hero */
.hero-title{left:140px;top:262px;width:440px;font-size:46px;font-weight:700;line-height:51px}
.hero-title em{font-style:normal;color:var(--pink)}
.hero-text{left:140px;top:540px;width:370px;font-size:16px;line-height:27px;color:var(--ink)}

/* story */
.section-title{font-size:34px;font-weight:700}
.story-text p{font-size:13px;line-height:21px;margin-bottom:14px}

/* mission cards */
.info-card{border-radius:22px;background:var(--card)}
.info-card .icon{width:128px;height:128px;border-radius:50%;display:flex;align-items:center;justify-content:center}
.info-card .icon svg{width:72px;height:72px;fill:none;stroke:var(--ink);stroke-width:2.5}
.info-card h2{font-size:32px;font-weight:600;margin:10px 0 18px}
.info-card p{font-size:12px;line-height:20.5px}

/* team */
.center{text-align:center;left:0;width:1200px}
.team-card{width:186px;height:290px;background:#fff;border-radius:14px;box-shadow:0 4px 14px rgba(0,0,0,.07);overflow:hidden;text-align:center}
.team-card .dog{height:228px;border-radius:14px 14px 0 0}
.team-card .name{font-family:"Outfit",sans-serif;font-size:16px;font-weight:600;margin-top:8px}
.team-card .role{font-size:11px;color:var(--ink)}

/* donors */
.donor-card{width:320px;height:360px;background:#fff;border-radius:16px;box-shadow:0 3px 14px rgba(0,0,0,.06);padding:0 40px}
.donor-card .badge{width:68px;height:68px;border-radius:50%;margin:18px auto 28px;display:flex;align-items:center;justify-content:center}
.donor-card .badge svg{width:34px;height:34px;fill:none;stroke:#fff;stroke-width:2}
.donor-card h3{font-size:17px;font-weight:600;margin-bottom:14px}
.donor-card ul{list-style:none}
.donor-card li{font-size:13px;font-weight:600;color:var(--ink);padding-left:14px;position:relative;margin-bottom:11px}
.donor-card li::before{content:"";position:absolute;left:0;top:8px;width:5px;height:5px;border-radius:50%;background:var(--ink)}
.donor-card li span{display:block;font-size:11px;font-weight:400;color:var(--text);line-height:17px;margin-top:3px}

/* thanks band */
.thanks{left:80px;top:2932px;width:1025px;height:262px;background:var(--pink-band);border-radius:20px;overflow:hidden}
.thanks p{position:absolute;left:68px;width:440px;color:#fff;font-size:15px;line-height:24px}

/* footer */
.footer{left:0;top:3255px;width:1200px;height:285px;background:var(--footer)}
.footer h4{font-family:"Outfit",sans-serif;font-size:15px;font-weight:600;color:var(--ink);margin-bottom:16px}
.footer ul{list-style:none}
.quick li{font-size:11.5px;color:var(--ink);margin-bottom:11px;display:flex;gap:12px;align-items:center}
.contact li{font-size:11.5px;color:var(--ink);margin-bottom:16px;display:flex;gap:16px;align-items:center}
.contact svg{width:18px;height:18px;fill:none;stroke:var(--ink);stroke-width:1.8}
.social{display:flex;gap:14px}
.social span{width:32px;height:32px;border-radius:50%;border:1.6px solid var(--ink)}
.field{width:258px;height:38px;border:1px solid #e3dfd8;border-radius:8px;background:#fff;font-size:11px;color:var(--muted);padding:0 14px;display:flex;align-items:center}
.legal{left:0;top:3540px;width:1200px;height:52px;font-size:10px;color:var(--text)}
</style>
</head>
<body>
<svg width="0" height="0" style="position:absolute">
  <symbol id="paw" viewBox="0 0 24 24"><ellipse cx="6" cy="9" rx="2.3" ry="3"/><ellipse cx="10.5" cy="5.5" rx="2.3" ry="3"/><ellipse cx="15.5" cy="5.5" rx="2.3" ry="3"/><ellipse cx="20" cy="9" rx="2.3" ry="3"/><path d="M13 11c-4 0-7 5-6 8 1 2 4 1 6 1s5 1 6-1c1-3-2-8-6-8z"/></symbol>
  <symbol id="heart" viewBox="0 0 24 24"><path d="M12 21s-8-5.5-8-11a4.5 4.5 0 0 1 8-2.8A4.5 4.5 0 0 1 20 10c0 5.5-8 11-8 11z"/></symbol>
</svg>

<!-- Header -->
<header>
  <div class="abs logo" style="left:55px;top:58px">
    <span class="logo-mark"></span>
    <div><div class="logo-name">Hollow Birch</div><div class="logo-sub">Therapy Dogs</div></div>
  </div>
  <nav class="abs top-links">
    <a href="#"><svg viewBox="0 0 24 24"><use href="#heart"/></svg>Join Now</a>
    <a href="#"><svg viewBox="0 0 24 24"><circle cx="12" cy="12" r="8"/></svg>Donate Now</a>
    <a href="#"><svg viewBox="0 0 24 24"><rect x="4" y="5" width="16" height="15" rx="2"/><path d="M4 10h16"/></svg>Request a Visit</a>
    <a href="#"><svg viewBox="0 0 24 24"><rect x="3" y="6" width="18" height="13" rx="2"/><path d="M3 7l9 6 9-6"/></svg>Contact Us</a>
  </nav>
  <nav class="abs nav">
    <a class="active" href="#">HOME</a><a href="#">OUR STORY</a><a href="#">OUR TEAM</a><a href="#">GET INVOLVED</a><a href="#">DONORS &amp; REFERRALS</a><a href="#">CONTACT US</a>
  </nav>
  <svg class="abs paw" style="left:346px;top:146px;color:var(--pink)"><use href="#paw"/></svg>
</header>

<!-- Hero -->
<section>
  <h1 class="abs hero-title">Bringing Comfort, <em>joy and unconditional love –</em> One Paw at a time.</h1>
  <p class="abs hero-text">A Michigan Nonprofit dedicated to providing Therapy Dogs to the community to spread joy, hope and healing.</p>
  <a class="abs btn" style="left:140px;top:659px" href="#">Request a Visit <svg class="paw"><use href="#paw"/></svg></a>
  <svg class="abs" style="left:30px;top:640px;width:80px;height:80px;fill:var(--pink-soft)"><use href="#paw" x="0" y="0" width="30" height="30"/><use href="#paw" x="34" y="34" width="30" height="30"/></svg>
  <svg class="abs" style="left:495px;top:490px;width:44px;height:40px;fill:none;stroke:var(--pink);stroke-width:1.5"><use href="#heart"/></svg>
  <svg class="abs" style="left:580px;top:300px;width:560px;height:445px" viewBox="0 0 560 445">
    <path d="M60 60C150 10 300 40 400 60s160 80 150 200-60 180-200 185H80C20 420 0 320 10 230S-20 110 60 60z" fill="var(--pink-soft)"/>
    <path d="M400 345c40-40 120-50 150-20v120H390c-20-30-20-70 10-100z" fill="var(--yellow)"/>
  </svg>
  <div class="abs photo" role="img" aria-label="Golden retriever wearing a pink bandana" style="left:615px;top:215px;width:360px;height:530px;border-radius:180px 180px 20px 20px"></div>
</section>

<!-- Our Story -->
<section>
  <div class="abs photo" role="img" aria-label="Girl hugging a fluffy golden dog in a field" style="left:100px;top:835px;width:430px;height:395px;border-radius:48% 52% 45% 55% / 45% 40% 60% 55%;background:linear-gradient(135deg,#c7ab7a,#8c6b45)"></div>
  <svg class="abs" style="left:108px;top:855px;width:52px;height:46px;fill:none;stroke:var(--green);stroke-width:2"><use href="#heart"/></svg>
  <svg class="abs" style="left:475px;top:1165px;width:70px;height:80px;fill:var(--pink-soft)"><use href="#paw" x="30" y="0" width="30" height="30"/><use href="#paw" x="0" y="34" width="30" height="30"/><use href="#paw" x="36" y="46" width="30" height="30"/></svg>
  <div class="abs story-text" style="left:600px;top:842px;width:410px">
    <div class="eyebrow"><svg class="paw" style="width:11px;height:11px"><use href="#paw"/></svg>Our Story</div>
    <h2 class="section-title" style="margin:14px 0 18px">Our Story</h2>
    <p>Every wag tells a story – and ours began with a simple belief: the love of a dog can change lives.</p>
    <p>What started with a few volunteers and their dogs has grown into a community dedicated to bringing comfort and joy wherever it's needed most. From hospitals to schools and senior centers, our therapy dog teams share moments of connection, calm, and healing – one visit at a time.</p>
    <p>At the heart of our mission is a simple truth – sometimes the best kind of therapy comes with four paws and a wagging tail.</p>
    <a class="btn" style="height:38px;margin-top:8px" href="#">Learn More <svg class="paw"><use href="#paw"/></svg></a>
  </div>
</section>

<!-- Mission & Purpose -->
<section>
  <div class="abs info-card" style="left:80px;top:1328px;width:510px;height:420px">
    <div class="abs icon" style="left:46px;top:50px;background:var(--green-soft)"><svg viewBox="0 0 48 48"><path d="M24 24s-7-4.5-7-9a3.5 3.5 0 0 1 7-1.5 3.5 3.5 0 0 1 7 1.5c0 4.5-7 9-7 9z"/><path d="M6 22v10l9 10M42 22v10l-9 10M12 26l6 8M36 26l-6 8"/></svg></div>
    <div class="abs" style="left:200px;top:64px;width:275px">
      <div class="eyebrow green"><svg class="paw" style="width:11px;height:11px"><use href="#paw"/></svg>Our Mission</div>
      <h2>Our Mission</h2>
      <p>To certify, and deploy therapy dog teams that promote emotional well-being, reduce stress, and foster empathy. We are dedicated to improving quality of life by bringing the unconditional love and calming presence of therapy dogs to those in need, while upholding the highest standards of animal welfare, professionalism, and community service.</p>
    </div>
  </div>
  <div class="abs info-card" style="left:608px;top:1328px;width:510px;height:420px;background:#fdfbf5">
    <div class="abs icon" style="left:46px;top:50px;background:var(--yellow-soft)"><svg viewBox="0 0 48 48"><circle cx="17" cy="12" r="5"/><circle cx="31" cy="12" r="5"/><path d="M8 40V26a9 9 0 0 1 18 0M22 40V26a9 9 0 0 1 18 0"/></svg></div>
    <div class="abs" style="left:200px;top:64px;width:260px">
      <div class="eyebrow gold"><svg class="paw" style="width:11px;height:11px"><use href="#paw"/></svg>Our Purpose</div>
      <h2>Our Purpose</h2>
      <p>Our purpose is to share the comfort, joy, and healing power of the human animal bond. We connect trained therapy dog teams with people in need of emotional support, companionship, and encouragement in hospitals, schools, senior communities, and beyond. Through every visit, we aim to lift spirits, ease stress, and remind people that kindness and connection can come on four paws and a wagging tail.</p>
    </div>
    <svg class="abs" style="left:485px;top:372px;width:40px;height:36px;fill:none;stroke:var(--green);stroke-width:2"><use href="#heart"/></svg>
  </div>
</section>

<!-- Team -->
<section>
  <div class="abs center" style="top:1796px">
    <div class="eyebrow" style="justify-content:center"><svg class="paw" style="width:11px;height:11px"><use href="#paw"/></svg>Our Team</div>
    <h2 class="section-title" style="margin:10px 0 10px">Our Team</h2>
    <p style="font-size:12px;line-height:19px;color:var(--ink)">A group of passionate volunteers and their amazing dogs<br>making a difference, one visit at a time.</p>
  </div>
  <svg class="abs" style="left:0;top:1850px;width:70px;height:110px;fill:var(--pink-soft)"><use href="#paw" x="20" y="0" width="40" height="40"/><use href="#paw" x="6" y="58" width="48" height="48"/></svg>
  <div class="abs team-card" style="left:80px;top:1960px"><div class="dog" role="img" aria-label="Curly golden doodle in a pink bandana" style="background:linear-gradient(160deg,#ead8be,#a7703f)"></div><div class="name" style="color:var(--pink)">Bailey</div><div class="role">Comfort Buddy</div></div>
  <div class="abs team-card" style="left:290px;top:1960px"><div class="dog" role="img" aria-label="Black labrador in a green bandana" style="background:linear-gradient(160deg,#eeeae3,#2a2624)"></div><div class="name" style="color:var(--green)">Cooper</div><div class="role">Smiles Provider</div></div>
  <div class="abs team-card" style="left:500px;top:1960px"><div class="dog" role="img" aria-label="Golden retriever in a pink bandana" style="background:linear-gradient(160deg,#f1e4d2,#cf9a5c)"></div><div class="name" style="color:var(--pink)">Daisy</div><div class="role">Joy Spreader</div></div>
  <div class="abs team-card" style="left:710px;top:1960px"><div class="dog" role="img" aria-label="Bernese mountain dog in a green bandana" style="background:linear-gradient(160deg,#eeeae3,#4a3326)"></div><div class="name" style="color:var(--green)">Luna</div><div class="role">Calm Companion</div></div>
  <div class="abs team-card" style="left:920px;top:1960px"><div class="dog" role="img" aria-label="Shih tzu in a pink bandana" style="background:linear-gradient(160deg,#f1ece6,#c7a98b)"></div><div class="name" style="color:var(--pink)">Teddy</div><div class="role">Little Healer</div></div>
  <a class="abs btn green" style="left:498px;top:2282px;height:40px" href="#">Meet Our Team <svg class="paw"><use href="#paw"/></svg></a>
</section>

<!-- Donors -->
<section>
  <div class="abs center" style="top:2368px">
    <div class="eyebrow" style="justify-content:center"><svg class="paw" style="width:11px;height:11px"><use href="#paw"/></svg>Donors &amp; Referrals</div>
    <h2 class="section-title" style="margin:14px 0 14px">Donors &amp; Referrals</h2>
    <p style="font-size:12px;line-height:20px;color:var(--text)">Our donors and referral partners are the heart of our organization. Because of their generosity,<br>we are able to keep costs low for our therapy dog teams while never compromising the<br>integrity, training, and care of our handlers and dogs.</p>
  </div>
  <svg class="abs" style="left:1062px;top:2450px;width:68px;height:60px;fill:none;stroke:var(--pink);stroke-width:1.6"><use href="#heart"/></svg>

  <div class="abs donor-card" style="left:93px;top:2540px">
    <div class="badge" style="background:var(--pink)"><svg viewBox="0 0 24 24"><use href="#heart"/></svg></div>
    <h3 style="color:var(--pink)">Corporate Donors</h3>
    <ul>
      <li>Brightline Tech<span>Cloud Phone Systems Built for Reliable Business Communications</span></li>
      <li>Harbor Ridge Veterans Post 12<span>Serving Veterans from the local community since 1930.<br>To all who have served America: THANK YOU!</span></li>
    </ul>
  </div>
  <div class="abs donor-card" style="left:432px;top:2540px">
    <div class="badge" style="background:var(--green)"><svg viewBox="0 0 24 24"><circle cx="8" cy="9" r="3"/><circle cx="16" cy="9" r="3"/><path d="M3 19a5 5 0 0 1 10 0M11 19a5 5 0 0 1 10 0"/></svg></div>
    <h3 style="color:var(--green)">Individual Donors</h3>
    <ul>
      <li>Martin Greer</li><li>Owen Fairley</li><li>Walter Greer</li><li>Janet Holloway</li><li>Carol Whitby</li><li>Dean Greer</li><li>Glen Ashford</li>
    </ul>
  </div>
  <div class="abs donor-card" style="left:772px;top:2540px">
    <div class="badge" style="background:var(--yellow)"><svg viewBox="0 0 24 24"><path d="M3 12l5-5 4 3 4-3 5 5-9 8z"/></svg></div>
    <h3 style="color:#e0a12b">Referrals</h3>
    <ul>
      <li>Steadfast Canine Training<span>Northern Michigan Dog Training Facility<br>Bridging the communication gap between dogs &amp; owners.</span></li>
    </ul>
  </div>
</section>

<!-- Thanks band -->
<section class="abs thanks">
  <p style="top:64px;color:#fff3f6">Every visit, every wagging tail, and every moment of comfort is made possible by your kindness, our dedicated volunteers, and a whole lot of furry friends and helping paws.</p>
  <p style="top:170px;font-weight:600;font-size:16px">Thank you for believing in our mission and helping us spread healing one paw at a time.</p>
  <svg class="abs" style="left:528px;top:172px;width:38px;height:34px;fill:none;stroke:#fff;stroke-width:1.6"><use href="#heart"/></svg>
  <div class="abs" role="img" aria-label="Boy hugging a golden retriever" style="left:580px;top:0;width:445px;height:262px;background:linear-gradient(110deg,var(--pink-band) 0%,#e8c08f 35%,#c48a52 100%)"></div>
</section>

<!-- Footer -->
<footer class="abs footer">
  <div class="abs logo" style="left:68px;top:75px">
    <span class="logo-mark"></span>
    <div><div class="logo-name">Hollow Birch</div><div class="logo-sub">Therapy Dogs</div></div>
  </div>
  <div class="abs social" style="left:73px;top:196px" aria-label="Social links"><span></span><span></span><span></span><span></span></div>
  <div class="abs quick" style="left:378px;top:50px">
    <h4>Quick Links</h4>
    <ul>
      <li><svg class="paw" style="width:12px;height:12px;fill:var(--ink)"><use href="#paw"/></svg>Home</li>
      <li><svg class="paw" style="width:12px;height:12px;fill:var(--ink)"><use href="#paw"/></svg>Our Story</li>
      <li><svg class="paw" style="width:12px;height:12px;fill:var(--ink)"><use href="#paw"/></svg>Our Team</li>
      <li><svg class="paw" style="width:12px;height:12px;fill:var(--ink)"><use href="#paw"/></svg>Get Involved</li>
      <li><svg class="paw" style="width:12px;height:12px;fill:var(--ink)"><use href="#paw"/></svg>Donors &amp; Referrals</li>
      <li><svg class="paw" style="width:12px;height:12px;fill:var(--ink)"><use href="#paw"/></svg>Contact Us</li>
    </ul>
  </div>
  <div class="abs contact" style="left:588px;top:50px">
    <h4>Contact Us</h4>
    <ul>
      <li><svg viewBox="0 0 24 24"><path d="M5 3h4l2 5-3 2a12 12 0 0 0 6 6l2-3 5 2v4a2 2 0 0 1-2 2A17 17 0 0 1 3 5a2 2 0 0 1 2-2z"/></svg>(555) 010-4477</li>
      <li><svg viewBox="0 0 24 24"><rect x="3" y="6" width="18" height="13" rx="2"/><path d="M3 7l9 6 9-6"/></svg>info@hollowbirch.org</li>
      <li><svg viewBox="0 0 24 24"><path d="M12 21s-7-7-7-12a7 7 0 0 1 14 0c0 5-7 12-7 12z"/><circle cx="12" cy="9" r="2.5"/></svg>Cedar Hollow, Michigan</li>
      <li><svg viewBox="0 0 24 24"><circle cx="12" cy="12" r="9"/><path d="M12 7v5l3 2"/></svg>Mon – Fri: 9am – 5pm</li>
    </ul>
  </div>
  <div class="abs" style="left:864px;top:50px;width:260px">
    <h4>Subscribe to Our Newsletter</h4>
    <p style="font-size:11px;line-height:19px;color:var(--ink);margin-bottom:18px">Stay updated on our visits, events<br>and heartwarming stories.</p>
    <div class="field">Enter your email address</div>
    <a class="btn" style="width:258px;justify-content:center;height:38px;margin-top:12px" href="#">Subscribe <svg class="paw"><use href="#paw"/></svg></a>
  </div>
</footer>
<div class="abs legal">
  <span class="abs" style="left:75px;top:20px">© 2024 Hollow Birch Therapy Dogs. All rights reserved.</span>
  <span class="abs" style="left:955px;top:20px">Privacy Policy &nbsp;&nbsp;&nbsp;|&nbsp;&nbsp;&nbsp; Terms of Use</span>
</div>
</body>
</html>
```